Flyer für mobile tierärztliche Ultraschalluntersuchungen
Zielgruppe
Mobile tierärztliche Ultraschalluntersuchungen, Zielgruppe: Tierärzt/Tierpraxen, die kein ultraschall Gerät od US-Kenntnisse haben.
Aufgabenstellung
1 Seite (recto D, verso F Sprache), professionell , seriös, aber optisch auffällig, damit es nicht direkt in Papierkorb landet.

```html
<!DOCTYPE html>
<html lang="fr">
<head>
<meta charset="utf-8">
<title>Service itinérant d'échographie vétérinaire</title>
<link href="https://fonts.googleapis.com/css2?family=Roboto+Condensed:wght@700&family=PT+Sans:wght@400;700&display=swap" rel="stylesheet">
<style>
  :root {
    --backdrop: #ece6e8;
    --paper-grey: #deddd8;
    --paper-white: #ffffff;
    --green-dark: #3d6a37;
    --green-mid: #5a9c4a;
    --green-pale: #d2e8c2;
    --text-green: #4a6e42;
    --accent-red: #d8322c;
    --photo-blue: #5b6f9c;
    --photo-skin: #b99a86;
  }
  * { margin: 0; padding: 0; box-sizing: border-box; }
  html, body { width: 1200px; height: 900px; overflow: hidden; background: var(--backdrop); }
  .flyer {
    position: absolute; left: 300px; top: 25px;
    width: 600px; height: 850px;
    background: var(--paper-grey);
    overflow: hidden;
    font-family: "PT Sans", sans-serif;
    color: var(--text-green);
  }
  .flyer__wave { position: absolute; inset: 0; }
  .logo-illustration {
    position: absolute; left: 445px; top: 22px;
    width: 125px; height: 125px; border-radius: 50%;
    background: var(--green-pale);
  }
  .header__name {
    position: absolute; left: 36px; top: 34px;
    font-family: "Roboto Condensed", sans-serif; font-weight: 700;
    font-size: 40px; color: var(--green-dark); letter-spacing: -0.5px;
  }
  .header__brand {
    position: absolute; left: 40px; top: 92px;
    font-family: "PT Sans", sans-serif; font-weight: 400;
    font-size: 30px; color: var(--green-mid);
    display: flex; align-items: center; gap: 10px;
  }
  .header__brand-dot { width: 14px; height: 14px; border-radius: 50%; background: var(--green-mid); }
  .header__rule {
    position: absolute; left: 36px; top: 142px; width: 500px; height: 2px;
    background: var(--green-dark);
  }
  .header__tagline {
    position: absolute; left: 36px; top: 150px;
    font-family: "Roboto Condensed", sans-serif; font-weight: 700;
    font-size: 22px; color: var(--green-dark);
  }
  .photo-ring { position: absolute; border-radius: 50%; background: var(--green-pale); }
  .photo-ring--exam { left: 8px; top: 230px; width: 300px; height: 300px; }
  .photo-ring--portrait { left: 345px; top: 548px; width: 290px; height: 290px; }
  .photo { position: absolute; inset: 12px; border-radius: 50%; }
  .photo--exam { background: linear-gradient(160deg, #e9e9ec 0%, #b9bfcf 40%, var(--photo-blue) 75%, #2f2f36 100%); }
  .photo--portrait { background: radial-gradient(circle at 45% 45%, var(--photo-skin) 0%, #6e5446 45%, #8d96a0 80%); }
  .services {
    position: absolute; left: 320px; top: 235px; width: 265px;
    list-style: none; font-size: 13px; line-height: 1.28;
  }
  .services li { position: relative; padding-left: 12px; margin-bottom: 6px; }
  .services li::before { content: "•"; position: absolute; left: 0; }
  .bio { position: absolute; left: 36px; top: 570px; width: 300px; }
  .bio__name {
    font-family: "Roboto Condensed", sans-serif; font-weight: 700;
    font-size: 25px; color: var(--green-dark); margin-bottom: 6px;
  }
  .bio__facts { list-style: none; font-size: 13px; line-height: 1.3; }
  .bio__facts li { position: relative; padding-left: 12px; margin-bottom: 4px; }
  .bio__facts li::before { content: "•"; position: absolute; left: 0; }
  .bio__call {
    margin-top: 10px; font-weight: 700; font-style: italic;
    font-size: 15px; color: var(--accent-red); line-height: 1.25;
  }
  .bio__contact { margin-top: 10px; font-size: 13px; line-height: 1.35; }
</style>
</head>
<body>
  <article class="flyer">
    <svg class="flyer__wave" width="600" height="850" viewBox="0 0 600 850" aria-hidden="true">
      <path d="M230 250 C330 190 450 230 600 160 L600 560 C520 580 440 560 390 620 C340 680 300 620 285 540 C270 440 255 340 230 250 Z" fill="var(--paper-white)"/>
      <path d="M480 20 C560 40 600 90 600 160 L600 0 L470 0 Z" fill="var(--paper-white)"/>
    </svg>

    <div class="logo-illustration" role="img" aria-label="Illustration: vétérinaire marchant avec un chien et une sacoche d'échographe"></div>

    <h1 class="header__name">Dr. med. vet. Léa Morand</h1>
    <div class="header__brand"><span class="header__brand-dot"></span>echo vet mobile</div>
    <div class="header__rule"></div>
    <p class="header__tagline">Service itinérant d'ECHOGRAPHIE vétérinaire</p>

    <div class="photo-ring photo-ring--exam">
      <div class="photo photo--exam" role="img" aria-label="Photo: vétérinaire pratiquant une échographie sur un chat"></div>
    </div>

    <ul class="services">
      <li>La prise de rendez-vous est flexible et rapide par email ou téléphone</li>
      <li>Je me déplace avec mon échographe de haute qualité Sonara active pour des échographies abdominales et thoraciques à votre cabinet</li>
      <li>Vos clients restent chez vous, pas de route à faire et la facturation se fait par votre cabinet</li>
      <li>Je m'occupe des chiens et de chats, mais aussi des NACs, incl. reptiles</li>
      <li>Nous pouvons discuter et échanger pour la prise en charge de votre patient</li>
      <li>Je parle quatre langues et les rapports peuvent se faire en français, allemand ou anglais</li>
    </ul>

    <div class="photo-ring photo-ring--portrait">
      <div class="photo photo--portrait" role="img" aria-label="Photo portrait de la vétérinaire"></div>
    </div>

    <section class="bio">
      <h2 class="bio__name">Dr. med. vet. Léa Morand</h2>
      <ul class="bio__facts">
        <li>Diplômée de l'Université du Jura-Sud en 2007</li>
        <li>Doctorat en pathologie de la faune sauvage</li>
        <li>Ayant plus de 10 ans de pratique clinique (animaux de compagnie et NACs)</li>
        <li>Suivant des formations continues en échographie en Suisse et à l'étranger</li>
      </ul>
      <p class="bio__call">Vous êtes curieux ?<br>Rencontrons-nous pour discuter !</p>
      <p class="bio__contact">Tél : +41 79 000 12 34<br>lmorand.vet@mailbox-demo.ch<br>www.echovet-mobile-demo.ch</p>
    </section>
  </article>
</body>
</html>
```